New Advertising Company Business Card

A two sided business card. One side with logo only and the other side with my information and maybe my logo again. Looking for something unique and creative, but not too busy. Info would include my name(Marcus Feldon), President, phone number, address, email address, and website. LOGO IS THE BLUE AND WHITE ONE.

Target Market(s)

CEO/VP Level Audience

Industry/Entity Type

Business

Contact Information for Business Card

In Description.

```html
<!DOCTYPE html>
<html lang="en">
<head>
<meta charset="UTF-8">
<title>Halvern Advertising — Business Card</title>
<link rel="stylesheet" href="https://fonts.googleapis.com/css2?family=Montserrat:wght@600&family=Arimo:wght@400&family=Roboto:wght@300&family=Tinos:wght@400&display=swap">
<style>
  :root {
    --backdrop: #6e6e6e;
    --card-white: #f3f3f1;
    --ink-dark: #1d1d1f;
    --ink-navy: #2a2760;
    --brand-blue: #1c6fc0;
    --bronze: #8a5b30;
    --bronze-light: #c39468;
    --glow: #f5f5f3;
  }
  * { margin: 0; padding: 0; box-sizing: border-box; }
  html, body {
    width: 1200px;
    height: 1200px;
    overflow: hidden;
    background: var(--backdrop);
  }
  .canvas {
    position: relative;
    width: 1200px;
    height: 1200px;
  }
  .card {
    position: absolute;
    left: 150px;
    width: 900px;
    height: 514px;
    box-shadow: 0 10px 30px rgba(0,0,0,0.35);
  }
  .card--info { top: 70px; background: var(--card-white); }
  .card--brand {
    top: 616px;
    background: radial-gradient(circle at 50% 50%,
      #c9a27c 0%,
      #dcc4ab 14%,
      var(--glow) 23%,
      #ece2d6 27%,
      #d6b897 36%,
      #b48352 50%,
      var(--bronze) 68%,
      #83552c 100%);
  }
  .wordmark {
    font-family: "Montserrat", sans-serif;
    font-weight: 600;
    color: var(--brand-blue);
    letter-spacing: 0.06em;
    text-transform: uppercase;
    display: flex;
    align-items: center;
    gap: 10px;
    white-space: nowrap;
  }
  .wordmark__dot {
    width: 12px;
    height: 12px;
    border-radius: 50%;
    background: var(--brand-blue);
    flex: none;
  }
  .card--info .wordmark {
    position: absolute;
    left: 70px;
    top: 100px;
    font-size: 19px;
  }
  .website {
    position: absolute;
    left: 70px;
    top: 400px;
    font-family: "Tinos", serif;
    font-size: 18px;
    color: var(--ink-navy);
  }
  .divider {
    position: absolute;
    left: 430px;
    top: 70px;
    width: 5px;
    height: 380px;
    background: linear-gradient(to bottom, var(--bronze) 0%, var(--bronze-light) 60%, rgba(195,148,104,0) 100%);
  }
  .identity {
    position: absolute;
    left: 520px;
    top: 150px;
  }
  .identity__name {
    font-family: "Arimo", sans-serif;
    font-weight: 400;
    font-size: 38px;
    color: var(--ink-dark);
  }
  .identity__title {
    font-family: "Roboto", sans-serif;
    font-weight: 300;
    font-size: 18px;
    color: var(--ink-navy);
    margin-top: 6px;
    letter-spacing: 0.02em;
  }
  .contact {
    position: absolute;
    left: 540px;
    top: 300px;
    list-style: none;
    font-family: "Tinos", serif;
    font-size: 16px;
    color: var(--ink-navy);
    line-height: 30px;
  }
  .card--brand .wordmark {
    position: absolute;
    left: 50%;
    top: 50%;
    transform: translate(-50%, -50%);
    font-size: 30px;
  }
  .card--brand .wordmark__dot { width: 16px; height: 16px; }
</style>
</head>
<body>
<main class="canvas">
  <section class="card card--info" aria-label="Card front with contact details">
    <div class="wordmark"><span class="wordmark__dot"></span>Halvern Advertising</div>
    <p class="website">www.xxxxx.com</p>
    <div class="divider"></div>
    <div class="identity">
      <h1 class="identity__name">Marcus Feldon</h1>
      <p class="identity__title">PRESIDENT</p>
    </div>
    <ul class="contact">
      <li>Phone no</li>
      <li>Adderess</li>
      <li>Email address</li>
    </ul>
  </section>
  <section class="card card--brand" aria-label="Card back with company name">
    <div class="wordmark"><span class="wordmark__dot"></span>Halvern Advertising</div>
  </section>
</main>
</body>
</html>
```